A4 Folder presentation Design Project

A4 Folder presentation Design.

A4 presentation folder, need to have company logo on it and aligned with company colors

Uploaded my business cards as a reference

Target Market(s)

Business owners

Industry/Entity Type

Electrical

Font styles to use
Sans Serif

Requirements
Must have
• Company logo

Company colors
Orange R:240 G:86 B:47
Blue R:4 G:116 B:187
Dark Grey

```html
<!DOCTYPE html>
<html lang="en">
<head>
<meta charset="UTF-8">
<title>Ridgeline Power – Presentation Folder</title>
<link rel="stylesheet" href="https://fonts.googleapis.com/css2?family=Montserrat:wght@400;700;800&family=Lato:wght@400&display=swap">
<style>
  :root {
    --orange: #f0562f;
    --blue: #0474bb;
    --dark: #1a1c1f;
    --white: #ffffff;
    --grey-band: #e2e2e2;
    --muted: #d9d9d9;
  }
  * { margin: 0; padding: 0; box-sizing: border-box; }
  html, body { width: 933px; height: 1200px; overflow: hidden; background: var(--dark); }
  .folder-cover {
    position: relative;
    width: 933px;
    height: 1200px;
    background: var(--dark);
    overflow: hidden;
  }
  .wave-art { position: absolute; inset: 0; width: 933px; height: 1200px; }
  .brand {
    position: absolute;
    left: 50px;
    top: 72px;
    display: flex;
    align-items: center;
    gap: 14px;
  }
  .brand-dot {
    width: 46px;
    height: 46px;
    border-radius: 50%;
    background: var(--orange);
  }
  .brand-name {
    font-family: "Montserrat", sans-serif;
    font-weight: 700;
    font-size: 30px;
    line-height: 1.05;
    letter-spacing: 0.5px;
    color: var(--blue);
    text-transform: uppercase;
  }
  .cover-text {
    position: absolute;
    left: 0;
    right: 0;
    top: 950px;
    text-align: center;
    color: var(--white);
  }
  .cover-title {
    font-family: "Montserrat", sans-serif;
    font-weight: 800;
    font-size: 47px;
    letter-spacing: 0.5px;
    line-height: 1.2;
  }
  .cover-intro {
    width: 660px;
    margin: 26px auto 0;
    font-family: "Lato", sans-serif;
    font-size: 15.5px;
    line-height: 22px;
  }
  .cover-url {
    position: absolute;
    left: 0;
    right: 0;
    top: 1167px;
    text-align: center;
    font-family: "Montserrat", sans-serif;
    font-weight: 400;
    font-size: 12.5px;
    letter-spacing: 0.3px;
    color: var(--muted);
  }
</style>
</head>
<body>
<main class="folder-cover">
  <svg class="wave-art" viewBox="0 0 933 1200" xmlns="http://www.w3.org/2000/svg">
    <defs>
      <linearGradient id="photoTone" x1="0" y1="0" x2="1" y2="0.3">
        <stop offset="0" stop-color="#6e2f1c"/>
        <stop offset="0.3" stop-color="#8d5a3e"/>
        <stop offset="0.55" stop-color="#b99b84"/>
        <stop offset="0.8" stop-color="#9b8f86"/>
        <stop offset="1" stop-color="#7d7670"/>
      </linearGradient>
    </defs>

    <path class="photo-area" role="img" aria-label="Photo: electrical technician in hard hat, safety glasses and hi-vis vest holding a laptop beside an open control panel"
      fill="url(#photoTone)"
      d="M0,0 H933 V780 C890,800 830,830 760,840 C700,850 640,840 580,800 C520,760 470,722 400,728 C340,735 320,815 260,830 C180,850 90,830 0,785 Z"/>

    <path class="bottom-swoosh" fill="var(--orange)" stroke="var(--white)" stroke-width="5"
      d="M0,785 C90,830 180,850 260,830 C320,815 340,735 400,728 C470,722 520,760 580,800 C640,840 700,850 760,840 C830,830 890,800 933,780
         L933,790 C880,820 820,855 760,858 C700,862 650,862 590,835 C530,805 480,760 410,765 C350,770 330,835 260,848 C180,862 100,848 0,802 Z"/>

    <path class="top-field" fill="var(--dark)" stroke="var(--white)" stroke-width="5"
      d="M0,0 H933 V40 C920,70 890,120 840,140 C780,160 720,135 640,135 C560,135 510,160 450,240 C400,310 360,355 290,345 C200,330 90,345 0,388 Z"/>

    <path class="grey-swoosh" fill="var(--grey-band)"
      d="M0,390 C90,348 200,333 290,348 C360,358 400,312 448,244 L470,256 C420,330 380,382 300,380 C200,370 100,372 0,404 Z"/>

    <path class="orange-swoosh" fill="var(--orange)"
      d="M452,238 C510,162 560,138 640,138 C720,138 780,163 840,143 C890,123 920,73 933,44 V188 C860,206 780,192 700,202 C600,212 540,252 470,332 C445,358 425,370 402,374 C430,332 445,295 452,238 Z"/>
  </svg>

  <header class="brand">
    <span class="brand-dot"></span>
    <span class="brand-name">Ridgeline<br>Power</span>
  </header>

  <section class="cover-text">
    <h1 class="cover-title">PRESENTATION NAME</h1>
    <p class="cover-intro">Lorem ipsum dolor sit amet, consectetur adipisicing elit, sed do eiusmod tempor incididunt ut labore et dolore magna aliqua. Ut enim ad minim veniam.</p>
  </section>

  <footer class="cover-url">www.ridgeline-brightgrid.com.au</footer>
</main>
</body>
</html>
```